BrXpertz Business Cards for SME Experts

We need a business card for a new company based in Clearwater FL called Kestrel of Merit. KoM is your access to on-demand subject matter experts. The final design should be very clean communicating innovation and expertise. Our logo design is attached.

The Information Age has affected the workforce in that automation and computerization have resulted in higher productivity coupled with net job loss of many knowledgeable employees. Combined with the creation of the internet and search capabilities, the disintermediation of the value chain of Subject Matter Experts (SME) has happened. We no longer need to work through traditional consulting firms for all consulting needs, instead the direct access to the SME, through a leaner and lower cost model is what the market is demanding.
BrXpertz is a new marketplace to buy consulting services. The business model is that all consultants (subject matter experts) can become a consulting resource in the marketplace following our guidelines. The consumer can now easily access consultants that they could not find easily before.
In much the way an Zyla car can be identified and requested, so can a BrXpertz Consultant. Each consultant can be identified by: location, expertise, billing rate, and prior experience rating.
By seamlessly connecting consultants to requesters through a new Kestrel of Merit marketplace, you now will have an easy to use and quicker turnaround to request and staff your consulting needs. Leveraging the KoM app, you can access the subject matter expert you need for your business requirement.

Target Market(s)

Small and medium sized companies; non-profits

Industry/Entity Type

Business Consultant

Contact Information for Business Card

Name
website
email address
Logo
mailing address (debating if I really need...)
twitter
LinkedIn

Requirements
Must have
• the logo I have included in the design; want the colors to be consistent with the logo design

```html
<!DOCTYPE html>
<html lang="en">
<head>
<meta charset="utf-8">
<title>Kestrel of Merit – Business Card</title>
<link rel="stylesheet" href="https://fonts.googleapis.com/css2?family=Exo+2:wght@600&family=Open+Sans:wght@400;600&display=swap">
<style>
  :root {
    --page-bg: #e9ecef;
    --navy: #16206a;
    --teal: #1ba3c6;
    --teal-dark: #117f9c;
    --teal-light: #2cb8d6;
    --white: #ffffff;
    --soft-white: #dfe6f5;
  }
  * { margin: 0; padding: 0; box-sizing: border-box; }
  html, body {
    width: 1200px; height: 950px; overflow: hidden;
    background: var(--page-bg);
    font-family: "Open Sans", sans-serif;
  }
  .sheet {
    width: 1200px; height: 950px;
    display: flex; flex-direction: column;
    align-items: center; justify-content: center; gap: 50px;
  }
  .card {
    position: relative;
    width: 700px; height: 400px;
    border-radius: 6px; overflow: hidden;
    box-shadow: 0 10px 28px rgba(22, 32, 106, 0.18);
  }

  /* Back */
  .card-back {
    background: linear-gradient(135deg, var(--teal-dark) 0%, var(--teal) 55%, var(--teal-light) 100%);
    display: flex; flex-direction: column; align-items: center; justify-content: center; gap: 20px;
  }
  .back-name {
    font-family: "Exo 2", sans-serif; font-weight: 600;
    font-size: 48px; color: var(--white); letter-spacing: 1px;
  }
  .back-web {
    font-size: 18px; letter-spacing: 2px; color: var(--white); opacity: .9;
  }

  /* Front */
  .card-front { background: var(--white); }
  .card-front .wave { position: absolute; inset: 0; }
  .brand {
    position: absolute; left: 70px; top: 96px;
    display: flex; align-items: center; gap: 14px;
  }
  .brand-dot {
    width: 26px; height: 26px; border-radius: 50%; background: var(--teal);
  }
  .brand-name {
    font-family: "Exo 2", sans-serif; font-weight: 600;
    font-size: 34px; color: var(--navy); letter-spacing: 1px;
  }

  .contact {
    position: absolute; right: 36px; top: 246px;
    display: flex; flex-direction: column; align-items: flex-end;
    color: var(--soft-white);
  }
  .social { display: flex; gap: 8px; margin-bottom: 6px; }
  .social span {
    width: 22px; height: 22px; border-radius: 50%; background: var(--teal);
  }
  .person-name { font-size: 22px; font-weight: 600; color: var(--teal-light); line-height: 1.2; }
  .person-role { font-size: 17px; margin-bottom: 4px; }
  .line { display: flex; align-items: center; gap: 10px; font-size: 16px; line-height: 1.5; }
  .line svg { width: 14px; height: 14px; flex: none; }
</style>
</head>
<body>
<main class="sheet">

  <section class="card card-back" aria-label="Card back">
    <p class="back-name">Kestrel of Merit</p>
    <p class="back-web">KestrelofMerit.com</p>
  </section>

  <section class="card card-front" aria-label="Card front">
    <svg class="wave" viewBox="0 0 700 400" preserveAspectRatio="none" aria-hidden="true">
      <path d="M0,222 C120,238 190,318 310,312 C430,306 500,226 620,222 L700,222 L700,400 L0,400 Z" fill="var(--navy)"/>
      <path d="M0,236 C110,252 180,316 300,308" fill="none" stroke="var(--teal)" stroke-width="5"/>
      <path d="M318,306 C440,296 510,226 700,218" fill="none" stroke="var(--navy)" stroke-width="2"/>
    </svg>

    <div class="brand">
      <span class="brand-dot"></span>
      <h1 class="brand-name">Kestrel of Merit</h1>
    </div>

    <div class="contact">
      <div class="social" aria-label="Social profiles">
        <span></span><span></span>
      </div>
      <p class="person-name">Dana Reyes</p>
      <p class="person-role">Consultant</p>
      <p class="line">Dana@KestrelofMerit.com
        <svg viewBox="0 0 14 14" aria-hidden="true"><rect x="1" y="3" width="12" height="8" fill="var(--teal)"/><path d="M1,3 L7,8 L13,3" fill="none" stroke="var(--navy)" stroke-width="1.2"/></svg>
      </p>
      <p class="line">KestrelofMerit.com
        <svg viewBox="0 0 14 14" aria-hidden="true"><circle cx="7" cy="7" r="6" fill="var(--teal)"/><path d="M1,7 H13 M7,1 C4,4 4,10 7,13 M7,1 C10,4 10,10 7,13" fill="none" stroke="var(--navy)" stroke-width="1"/></svg>
      </p>
    </div>
  </section>

</main>
</body>
</html>
```